Dubai Family protection infographic

We need to produce a way of attracting people to a life insurance and critical illness cover seminar. As this is a pretty dull subject for most people, so we need a cool way of getting people to read the invite/marketing collateral.

We're thinking some kind of colourful and attractive infographic that we can use on flyers and posters as well as online and as an emailer.

Content for the graphic is as bellow:

How much does it cost to replace Mum & Dad?

Mum = Chauffer, Cook, Laundry Service, Household Cleaner, Psychologist, Money Manager

Mums typically work a 94-hour week. At a rather paltry $12 per hour, that’s $4,888 per month – or $58,656 each year. (Source: wagelore.net)

Dad : The average Western Expat’s salary in the Gulf is $12,215 per month. That’s $146,580 each year. (Source: Palmcrest Ledger).

Did you know that the average age of critical illness claimants in the Middle East last year was just 48. Of these, 44% were for cancer while 41% were heart related.

The average age of a death claimant was just 50 years old.
(Source: Verenholt Assurance Group)

1 in 3 people will develop some form of cancer during their lifetime.

That’s 2.36 billion people globally.

And that’s equivalent to the population of China, USA, Brazil, Russia, Philippines, France, UK, South Africa and Italy combined.

Does your family have the resources to hand to cope if a tragedy happens to you?

What can you do to protect them and yourself?

Come to the UAE’s first national protection seminar to find out. Join us at Harbourline Riverside Sports Arena on June 19th at 19:00.

To pre-register, visit www.tovanmere.net/events or alternatively register on the door.

```html
<!DOCTYPE html>
<html lang="en">
<head>
<meta charset="utf-8">
<title>How much does it cost to replace Mum &amp; Dad?</title>
<link href="https://fonts.googleapis.com/css2?family=Arimo:wght@400;700&display=swap" rel="stylesheet">
<style>
  :root {
    --purple: #4b2c7f;
    --navy: #1d2f5c;
    --teal-dark: #245a62;
    --lime: #b9dc3c;
    --lime-light: #e4f2a8;
    --sky: #cfe7f4;
    --sky-deep: #8cc4e4;
    --silhouette: #2a3550;
    --green-figure: #5a9a3a;
    --white: #ffffff;
  }
  * { margin: 0; padding: 0; box-sizing: border-box; }
  html, body { width: 849px; height: 1200px; overflow: hidden; background: var(--white); }
  body { font-family: "Arimo", Arial, sans-serif; }
  .poster {
    position: relative; width: 849px; height: 1200px; overflow: hidden;
    background: radial-gradient(ellipse at 40% 45%, var(--white) 0%, var(--sky) 70%, var(--sky-deep) 100%);
  }
  .abs { position: absolute; }
  .header-band {
    left: 80px; top: 14px; width: 755px; height: 72px;
    background: linear-gradient(90deg, var(--lime-light), var(--lime) 60%, var(--sky-deep));
    border-radius: 4px; display: flex; align-items: center; justify-content: center;
  }
  .headline { font-size: 29px; font-weight: 700; color: var(--teal-dark); }

  .mum-roles { left: 40px; top: 110px; width: 420px; font-size: 20px; font-weight: 700; color: var(--purple); line-height: 1.2; }
  .mum-roles .lead { font-size: 56px; line-height: 1; }
  .mum-cost { left: 40px; top: 260px; width: 350px; font-size: 19px; font-weight: 700; color: var(--purple); line-height: 1.25; }
  .source { font-size: 14px; font-weight: 400; display: block; }

  .mum-icons { left: 36px; top: 400px; width: 360px; height: 70px; display: flex; gap: 14px; }
  .mum-icons div { width: 70px; height: 70px; border-radius: 50%; background: radial-gradient(circle, #f4e7a6, #e8a24a); }

  .dad-figure { left: 470px; top: 98px; width: 220px; height: 270px; border-radius: 110px 110px 20px 20px;
    background: linear-gradient(180deg, #3a4766, var(--silhouette)); }
  .dad-text { left: 530px; top: 378px; width: 300px; font-size: 19px; font-weight: 700; color: var(--purple); line-height: 1.25; }
  .dad-text .lead { font-size: 38px; line-height: 1; }

  .wheelchair-figure { left: 40px; top: 520px; width: 145px; height: 170px; border-radius: 60px 60px 10px 10px;
    background: linear-gradient(180deg, #3f4c6a, var(--silhouette)); }
  .illness-text { left: 200px; top: 525px; width: 310px; font-size: 19px; font-weight: 700; color: var(--purple); line-height: 1.25; }
  .illness-text .lead { font-size: 36px; line-height: 1.05; }
  .wheelchair-icon { left: 530px; top: 545px; width: 70px; height: 60px; border-radius: 8px; background: #7d8aa5; }

  .people-icons { left: 630px; top: 520px; width: 185px; height: 105px; border-radius: 10px;
    background: linear-gradient(90deg, #2f3a55 0%, #2f3a55 30%, var(--green-figure) 30%, var(--green-figure) 100%); }
  .cancer-text { left: 540px; top: 640px; width: 295px; font-size: 19px; color: var(--navy); line-height: 1.25; }
  .cancer-text .lead { font-size: 36px; }
  .cancer-text p { margin-top: 16px; font-weight: 400; }
  .cancer-text p:first-child { margin-top: 0; font-weight: 700; }

  .tower-figure { left: 40px; top: 720px; width: 130px; height: 450px; border-radius: 70px 20px 0 0;
    background: linear-gradient(180deg, #5a6b8c, var(--silhouette)); }
  .couple-figure { left: 335px; top: 690px; width: 180px; height: 170px; border-radius: 90px 90px 10px 10px;
    background: linear-gradient(180deg, #2b2b2b, #111); }
  .business-figure { left: 675px; top: 925px; width: 160px; height: 275px; border-radius: 80px 80px 0 0;
    background: linear-gradient(180deg, #4a5878, var(--silhouette)); }

  .question { left: 190px; top: 872px; width: 440px; text-align: center; font-size: 20px; font-weight: 700; color: var(--navy); line-height: 1.3; }
  .question p + p { margin-top: 10px; }

  .seminar-box { left: 250px; top: 1000px; width: 420px; padding: 12px 16px; background: var(--lime);
    text-align: center; color: var(--navy); font-size: 21px; font-weight: 700; line-height: 1.25; }
  .seminar-box .sub { font-size: 19px; }
  .register { left: 200px; top: 1140px; width: 460px; text-align: center; font-size: 16px; color: var(--navy); line-height: 1.3; }
</style>
</head>
<body>
<main class="poster">
  <div class="abs header-band"><h1 class="headline">How much does it cost to replace Mum &amp; Dad?</h1></div>

  <p class="abs mum-roles"><span class="lead">Mum</span> = Chauffer, Cook, Laundry Service, Household Cleaner, Psychologist, Money Manager</p>
  <p class="abs mum-cost">Mums typically work a 94-hour week. At a rather paltry $12 per hour, that’s $4,888 per month – or $58,656 each year. <span class="source">(Source: wagelore.net)</span></p>
  <div class="abs mum-icons" role="img" aria-label="Round icons of household chores: cooking, driving, laundry, cleaning, money">
    <div></div><div></div><div></div><div></div>
  </div>

  <div class="abs dad-figure" role="img" aria-label="Silhouette of a father lifting his child"></div>
  <p class="abs dad-text"><span class="lead">Dad:</span> The average Western Expat’s salary in the Gulf is $12,215 per month. That’s $146,580 each year. <span class="source">(Source: Palmcrest Ledger)</span></p>

  <div class="abs wheelchair-figure" role="img" aria-label="Silhouette of a person in a wheelchair"></div>
  <p class="abs illness-text"><span class="lead">Did you know</span> that the average age of critical illness claimants in the Middle East last year was just 48. Of these, 44% were for cancer while 41% were heart related.</p>
  <div class="abs wheelchair-icon" role="img" aria-label="Small wheelchair icon"></div>

  <div class="abs people-icons" role="img" aria-label="Row of three people figures, one dark and two green"></div>
  <div class="abs cancer-text">
    <p><span class="lead">1 in 3</span> will develop some form of cancer during their lifetime.</p>
    <p>That’s 2.36 billion people globally.</p>
    <p>And that’s equivalent to the population of China, USA, Brazil, Russia, Philippines, France, UK, South Africa and Italy combined.</p>
  </div>

  <div class="abs tower-figure" role="img" aria-label="Silhouette of a sail-shaped hotel tower"></div>
  <div class="abs couple-figure" role="img" aria-label="Silhouette of an elderly couple walking"></div>
  <div class="abs business-figure" role="img" aria-label="Silhouette of a businessman"></div>

  <div class="abs question">
    <p>Does your family have the resources to hand to cope if a tragedy happens to you?</p>
    <p>What can you do to protect them and yourself?</p>
  </div>

  <div class="abs seminar-box">
    <p>Come to the UAE’s first national protection seminar to find out.</p>
    <p class="sub">Join us at Harbourline Riverside Sports Arena on June 19th at 19:00.</p>
  </div>

  <p class="abs register">To pre-register, visit www.tovanmere.net/events or alternatively register on the door</p>
</main>
</body>
</html>
```